IT Networking and Communications Website

We are working with an IT Networking company in California. They install company networks, cabling, phone systems, etc...
A few websites for inspiration are included in the attachments.
Thank you for taking the time to consider designing a website for us. We are web developers based in Stockton, CA, USA. Most of our projects go through the same process. Understanding this process may help you win a project with us. We custom-code all of our websites in-house. We don’t have any requirements as to what tools you use for your design, but we ask that you follow these guidelines.
IMAGES:
If you use any images or icons in the design, we ask that you have a link to the asset so we can purchase the image/icon. Most of the designs we submit do not have the customer’s images on them unless they have some great images. Be creative; show us the feeling you are trying to portray with your image choices. Use any royalty-free site you choose. We subscribe to Velmora and mainly use their images, but we can purchase images outside of Velmora. PLEASE NOTE: we will not submit designs to clients with watermarks on the images.
FONTS:
We ask that you identify the fonts you’re using in the design. This can be done in a message if you want. We typically use Trinzel Fonts and Velmora Fonts.
CONTENT:
We're always open to different content and ideas. We often submit designs with stock images so the client can see our vision. We typically take pictures after the website launch to use their images with our vision. Lorem Ipsum is fine for paragraphs, but we ask that you make the Headers with correct English. We want to be able to show the vision and identify the sections of the website.
INSPIRATION:
We typically add a couple of links in the brief of websites we like to help you get started in your design.
REVISIONS:
We do not often ask for revisions of the designs unless we see something in the design that may not appeal to the client. If there are slight changes that we want to make, we do that in the development process.
FEEDBACK:
We rarely give feedback on designs during the design process. We are working on many website projects and do not have the time to provide feedback. We usually respond if your request is well thought out and asks specific questions, but a note asking “feedback, please” usually goes unanswered.

```html
<!DOCTYPE html>
<html lang="en">
<head>
<meta charset="utf-8">
<title>Bastion Business Communications</title>
<link href="https://fonts.googleapis.com/css2?family=EB+Garamond:wght@400;500&family=Roboto:ital,wght@0,400;0,500;0,700;1,400&family=Lato:wght@400&display=swap" rel="stylesheet">
<style>
:root{
  --navy:#0f2d40;
  --blue:#1f7fc4;
  --blue-dark:#1a4f8a;
  --text:#222;
  --muted:#555;
  --white:#fff;
  --gold:#f2b705;
  --line:#dcdcdc;
}
*{margin:0;padding:0;box-sizing:border-box}
html,body{width:1200px;height:3147px;overflow:hidden;background:var(--white);font-family:'Roboto',sans-serif;color:var(--text)}
.page{position:relative;width:1200px;height:3147px}
.abs{position:absolute}
.serif{font-family:'EB Garamond',serif;font-weight:500}

/* header */
.brand{position:absolute;display:flex;align-items:center;gap:10px;font-family:'EB Garamond',serif;font-weight:500;color:var(--blue-dark);font-size:27px;line-height:1}
.brand .dot{width:26px;height:26px;border-radius:50%;background:var(--blue-dark)}
.site-brand{left:112px;top:42px}
.main-nav{position:absolute;right:112px;top:36px;display:flex;gap:23px;font-size:15.5px;color:#333}

/* hero */
.hero{position:absolute;left:0;top:94px;width:1200px;height:471px;background:radial-gradient(ellipse at 40% 40%,#2d6a97 0%,#143a5a 45%,#0a1d2e 100%)}
.hero-text{position:absolute;right:391px;top:150px;text-align:right;color:var(--white);font-family:'EB Garamond',serif}
.hero-text .small{font-size:40px;line-height:1}
.hero-text h1{font-weight:500;font-size:58px;line-height:54px;margin-top:18px}
.btn-outline{position:absolute;display:flex;align-items:center;justify-content:center;border:2px solid var(--white);color:var(--white);font-weight:700;font-size:15px;letter-spacing:.3px}

/* section titles */
.section-title{position:absolute;left:0;width:1200px;text-align:center;font-family:'EB Garamond',serif;font-weight:500;font-size:48px;color:var(--navy)}
.divider{position:absolute;width:198px;height:12px}
.divider::before,.divider::after{content:"";position:absolute;top:5px;width:78px;height:2px;background:var(--blue)}
.divider::before{left:0}.divider::after{right:0}
.divider span{position:absolute;left:91px;top:0;width:16px;height:16px;border-radius:50%;background:var(--blue-dark)}

/* services */
.service{position:absolute;width:300px;text-align:center}
.service .icon{width:126px;height:126px;margin:0 auto;border-radius:50%;background:var(--white);box-shadow:0 6px 10px rgba(0,0,0,.18);display:flex;align-items:center;justify-content:center}
.service .icon i{display:block;width:70px;height:70px;border-radius:50%;background:linear-gradient(135deg,#d9ebf7,#b9d7ee)}
.service h3{margin-top:20px;font-size:16.5px;font-weight:500;color:#111}
.service p{font-family:'Lato',sans-serif;font-size:13px;line-height:25.5px;color:#333;margin-top:4px}
.btn-solid{position:absolute;display:flex;align-items:center;justify-content:center;background:linear-gradient(90deg,#1e86c6,#123e5c);color:var(--white);font-weight:700;font-size:15px}

/* bands */
.band{position:absolute;left:0;width:1200px;background:var(--navy)}
.about-band{top:1125px;height:510px;clip-path:polygon(0 27px,100% 0,100% 486px,0 100%)}
.blog-band{top:2240px;height:605px;clip-path:polygon(0 27px,100% 0,100% 578px,0 100%)}
.about-title{left:118px;top:1198px;color:var(--white);font-size:48px}
.about-copy{left:111px;top:1325px;width:452px;color:var(--white);font-size:15.5px;line-height:28.5px;text-align:justify}
.about-copy p+p{margin-top:7px}
.photo{position:absolute}

/* testimonials */
.avatar{position:absolute;width:95px;height:95px;border-radius:50%;border:2px solid #9dbcd8;background:linear-gradient(160deg,#c8d3df,#7d8ca0)}
.avatar.active{border:3px solid var(--navy);background:linear-gradient(160deg,#a8b8cc,#3d4f66)}
.avatar.faded{opacity:.55}
.quote{position:absolute;left:240px;top:1982px;width:720px;text-align:center;font-style:italic;font-size:17px;line-height:30px;color:#222}
.reviewer{position:absolute;left:0;top:2128px;width:1200px;text-align:center;font-size:17px;color:#111}
.stars{color:var(--gold);letter-spacing:2px;font-size:18px}
.qmark{position:absolute;font-family:'EB Garamond',serif;font-size:120px;line-height:1;color:#d6d6d6}

/* blog */
.post-photo{position:absolute;top:2460px;width:313px;height:206px}
.post-card{position:absolute;top:2607px;width:287px;height:161px;background:var(--white);padding:28px 20px 0 21px}
.post-card p{font-size:17px;line-height:28.5px;color:#555}
.post-card a{display:block;margin-top:6px;font-family:'EB Garamond',serif;font-size:19px;letter-spacing:.5px;color:var(--blue);text-decoration:none}

/* footer */
.footer-brand{left:117px;top:2900px;font-size:25px}
.footer-about{left:117px;top:2958px;width:280px;font-size:14px;line-height:25.5px;color:#222}
.footer-col h4{font-weight:400;font-size:16px;color:var(--blue)}
.footer-col h4::after{content:"";display:block;width:45px;height:1.5px;background:var(--blue);margin-top:9px}
.footer-col ul{list-style:none;margin-top:18px;font-size:13.5px;line-height:25.5px;color:#333}
.contact-list{list-style:none;margin-top:18px;font-size:13.5px;color:#333}
.contact-list li{display:flex;gap:12px;line-height:25.5px;margin-bottom:9px}
.contact-list svg{flex:none;margin-top:6px}
.footer-rule{position:absolute;left:117px;top:3095px;width:977px;height:1px;background:var(--line)}
.copyright{position:absolute;left:0;top:3111px;width:1200px;text-align:center;font-size:14px;color:#222}
</style>
</head>
<body>
<div class="page">

  <header>
    <div class="brand site-brand"><span class="dot"></span>Bastion Business Communications</div>
    <nav class="main-nav"><span>Home</span><span>Services</span><span>Industries</span><span>Why Us</span><span>Resources</span><span>Contact Us</span></nav>
  </header>

  <section class="hero" role="img" aria-label="Engineer working at monitors in a dimly lit server room">
    <div class="hero-text">
      <div class="small">Welcome to</div>
      <h1>Bastion Business<br>Communications</h1>
    </div>
  </section>
  <div class="btn-outline" style="left:534px;top:441px;width:132px;height:45px">GET QUOTE</div>

  <h2 class="section-title" style="top:622px">What we offer</h2>
  <div class="divider" style="left:501px;top:693px"><span></span></div>

  <div class="service" style="left:92px;top:753px">
    <div class="icon"><i role="img" aria-label="Network icon"></i></div>
    <h3>INSTALL COMPANY NETWORKS</h3>
    <p>Duis aute irure dolor in reprehender<br>it in voluptate velit esse cillum dolore<br>eu fugiat nulla pariatur.</p>
  </div>
  <div class="service" style="left:462px;top:753px">
    <div class="icon"><i role="img" aria-label="Cable icon"></i></div>
    <h3>CABLING</h3>
    <p>Duis aute irure dolor in reprehender<br>it in voluptate velit esse cillum dolore<br>eu fugiat nulla pariatur.</p>
  </div>
  <div class="service" style="left:820px;top:753px">
    <div class="icon"><i role="img" aria-label="Phone system icon"></i></div>
    <h3>PHONE SYSTEMS</h3>
    <p>Duis aute irure dolor in reprehender<br>it in voluptate velit esse cillum dolore<br>eu fugiat nulla pariatur.</p>
  </div>
  <div class="btn-solid" style="left:534px;top:1034px;width:132px;height:45px">VIEW ALL</div>

  <div class="band about-band"></div>
  <h2 class="abs serif about-title">About Us</h2>
  <div class="divider" style="left:111px;top:1271px"><span></span></div>
  <div class="abs about-copy">
    <p>Lorem ipsum dolor sit amet, consectetur adipiscing elit, sed do eiusmod tempor incididunt ut labore et dolore magna aliqua. Quis ipsum suspendisse ultrices gravida. Risus commodo viverra maecenas accumsan lacus vel facilisis.</p>
    <p>Quis ipsum suspendisse ultrices gravida. Risus commodo viverra maecenas accumsan lacus vel facilisis.</p>
  </div>
  <div class="btn-outline" style="left:111px;top:1526px;width:132px;height:45px">LEARN MORE</div>
  <div class="photo" role="img" aria-label="Technician touching a monitor in a warm-lit office" style="left:623px;top:1194px;width:294px;height:246px;background:linear-gradient(135deg,#6b4a2a,#d9a04a 55%,#f2d28a)"></div>
  <div class="photo" role="img" aria-label="Technician inspecting network cabling" style="left:792px;top:1300px;width:296px;height:356px;background:linear-gradient(160deg,#8a8278,#5c5a57 50%,#3a3c3f)"></div>

  <h2 class="section-title" style="top:1730px">Client Testimonials</h2>
  <div class="divider" style="left:501px;top:1802px"><span></span></div>
  <div class="avatar faded" role="img" aria-label="Client portrait" style="left:434px;top:1861px"></div>
  <div class="avatar active" role="img" aria-label="Client portrait" style="left:554px;top:1861px"></div>
  <div class="avatar faded" role="img" aria-label="Client portrait" style="left:674px;top:1861px"></div>
  <svg class="abs" style="left:34px;top:2015px" width="44" height="44" viewBox="0 0 44 44"><circle cx="22" cy="22" r="20" fill="none" stroke="#c9dcec" stroke-width="3"/><path d="M25 13l-9 9 9 9" fill="none" stroke="#c9dcec" stroke-width="3"/></svg>
  <svg class="abs" style="left:1122px;top:2015px" width="44" height="44" viewBox="0 0 44 44"><circle cx="22" cy="22" r="20" fill="none" stroke="#111" stroke-width="3"/><path d="M19 13l9 9-9 9" fill="none" stroke="#111" stroke-width="3"/></svg>
  <p class="quote">Nemo enim ipsam voluptatem quia voluptas sit aspernatur aut odit aut fugit, sed quia consequuntur magni dolores eos qui ratione voluptatem sequi nesciunt. Neque porro quisquam est, qui dolorem ipsum quia dolor sit amet, consectetur, adipisci velit, sed quia non numquam eius modi tempora incidunt ut labore et dolore magnam aliquam quaerat voluptatem.</p>
  <div class="reviewer">Mara Quill - <span class="stars">★★★★★</span></div>
  <div class="qmark" style="left:288px;top:2110px">“</div>
  <div class="qmark" style="left:852px;top:2110px">”</div>

  <div class="band blog-band"></div>
  <h2 class="section-title" style="top:2314px;color:var(--white)">Latest Blog</h2>
  <div class="divider" style="left:501px;top:2385px"><span></span></div>

  <div class="post-photo" role="img" aria-label="Technician wiring a server rack" style="left:112px;background:linear-gradient(135deg,#9aa3ab,#4a5560 60%,#c9a24a)"></div>
  <div class="post-photo" role="img" aria-label="Colleagues working at a computer in an office" style="left:445px;background:linear-gradient(135deg,#c4a58a,#6e5a48 55%,#2d2c2a)"></div>
  <div class="post-photo" role="img" aria-label="Glowing circuit board close-up" style="left:777px;background:linear-gradient(135deg,#1a1038,#3a2c8a 45%,#1fa6b8 80%,#e07a30)"></div>
  <div class="post-card" style="left:125px"><p>Duis aute irr in reprehenderit in voluptate velit esse cille dolore eu fugiat nulla. pariatur.</p><a>READ MORE &nbsp;⟶</a></div>
  <div class="post-card" style="left:458px"><p>Duis aute irr in reprehenderit in voluptate velit esse cille dolore eu fugiat nulla. pariatur.</p><a>READ MORE &nbsp;⟶</a></div>
  <div class="post-card" style="left:790px"><p>Duis aute irr in reprehenderit in voluptate velit esse cille dolore eu fugiat nulla. pariatur.</p><a>READ MORE &nbsp;⟶</a></div>

  <footer>
    <div class="brand footer-brand"><span class="dot"></span>Bastion Business<br>Communications</div>
    <p class="abs footer-about">At vero eos et accusamus et iusto dignissi mos ducimus qui blandits praesentium voluptatum corrupti dolores et quasmo lestias exceptt occaecati cupiditate nont.</p>

    <div class="abs footer-col" style="left:481px;top:2880px;width:260px">
      <h4>CONTACT INFO</h4>
      <ul class="contact-list">
        <li><svg width="11" height="14" viewBox="0 0 11 14"><path d="M5.5 0A5.5 5.5 0 0 0 0 5.5C0 9.5 5.5 14 5.5 14S11 9.5 11 5.5A5.5 5.5 0 0 0 5.5 0zm0 7.5a2 2 0 1 1 0-4 2 2 0 0 1 0 4z" fill="#0f2d40"/></svg><span>Bastion Business Communications,<br>Address comes here.</span></li>
        <li><svg width="10" height="15" viewBox="0 0 10 15"><rect x="0.5" y="0.5" width="9" height="14" rx="1.5" fill="none" stroke="#0f2d40"/><circle cx="5" cy="12" r="1" fill="#0f2d40"/></svg><span>Tel: +1 555-014-2290</span></li>
        <li><svg width="14" height="11" viewBox="0 0 14 11"><rect width="14" height="11" rx="1" fill="#0f2d40"/><path d="M1 1.5l6 4.5 6-4.5" fill="none" stroke="#fff" stroke-width="1.2"/></svg><span>info@bastionbizcom.com</span></li>
      </ul>
    </div>
    <div class="abs footer-col" style="left:796px;top:2880px">
      <h4>QUICK LINKS</h4>
      <ul><li>Home</li><li>Services</li><li>Industries</li><li>Why Us</li><li>Resources</li></ul>
    </div>
    <div class="abs footer-col" style="left:968px;top:2880px">
      <h4>OTHER LINKS</h4>
      <ul><li>Contact Us</li><li>Terms &amp; Conditions</li><li>Privacy Policy</li></ul>
    </div>
    <div class="footer-rule"></div>
    <p class="copyright">2023 Bastion Business Communications. All Rights Reserved.</p>
  </footer>

</div>
</body>
</html>
```